Letterhead for Business Law Firm

We need a letter head for our firm based on the design we have settled on and it is attached. Our clients are small and large businesses around the world, and our letterhead is used typically for formal legal purposes such as demand letters (accusing the recipient of doing bad things) or responding to demand letters. It may also be sent to regulators and other government agencies. So this needs to be tasteful, but a little edgy as well - we try to convey that we are a firm that is different - businesses and investors come to us for creative, quick advice, typically in high stress circumstances, and for our ability to work through high conflict situations, and rapid paced engagements.

Target Market(s)

Lawyers, business executives, investors, government regulators who may receive letters from this firm on behalf of its clients.

Industry/Entity Type

Business

Requirements
Must have
• The design and the firm's contact information:
• Quillfen Law Firm, P.C.
• 8716 SW 19th Ave
• Portland, OR 97058
• phone: 971 555 0143
• fax: 971 555 0178
• in what placement and how depicted (e.g. a phone icon instead of the word "phone") I leave to your creative ideas.
Nice to have
• design and information can be placed at the top, bottom and/or sides of the letter, and the design should be for a standard letter size paper - and can have a separate design for the second page.

```html
<!DOCTYPE html>
<html lang="en">
<head>
<meta charset="utf-8">
<title>Quillfen Law Firm, P.C. — Letterhead</title>
<link rel="stylesheet" href="https://fonts.googleapis.com/css2?family=Arimo:wght@400;700&display=swap">
<style>
  :root {
    --paper: #ffffff;
    --ink: #1b1f20;
    --teal: #4f9e8f;
    --stone: #c3cccb;
    --rule: #bcd8d2;
    --divider: #8a8f90;
  }
  * { margin: 0; padding: 0; box-sizing: border-box; }
  html, body { width: 933px; height: 1200px; overflow: hidden; background: var(--paper); }
  .letterhead {
    position: relative; width: 933px; height: 1200px; background: var(--paper);
    font-family: "Arimo", Arial, sans-serif; color: var(--ink);
  }
  .brand { position: absolute; left: 62px; top: 84px; display: flex; align-items: center; gap: 16px; }
  .brand-mark { width: 40px; height: 40px; background: var(--teal); flex: none; }
  .brand-name {
    display: flex; flex-direction: column; gap: 10px;
    font-weight: 400; color: var(--ink); line-height: 1; text-transform: uppercase;
  }
  .brand-name .firm { font-size: 40px; letter-spacing: 9px; }
  .brand-name .entity { font-size: 13px; letter-spacing: 6.2px; }
  .contact-top { position: absolute; left: 648px; top: 104px; list-style: none; }
  .contact-top li, .contact-bottom li {
    display: flex; align-items: center; height: 22px; font-size: 13px; color: var(--ink);
    white-space: nowrap;
  }
  .icon { width: 16px; height: 16px; flex: none; fill: var(--teal); }
  .sep { width: 1px; height: 15px; background: var(--divider); margin: 0 12px 0 10px; flex: none; }
  .rule-top { position: absolute; left: 61px; top: 177px; width: 811px; height: 1px; background: var(--rule); }
  .rule-bottom { position: absolute; left: 61px; top: 1077px; width: 376px; height: 1px; background: var(--stone); }
  .contact-bottom { position: absolute; left: 60px; top: 1086px; list-style: none; }
  .contact-bottom li { height: 27px; font-size: 14.5px; }
  .contact-bottom strong { font-weight: 700; margin-left: 4px; }
  .contact-bottom .label { font-weight: 700; margin-right: 5px; }
  .contact-bottom .gap { margin: 0 8px; color: var(--divider); }
  .branch-art {
    position: absolute; left: 460px; top: 603px; width: 473px; height: 597px;
    background:
      radial-gradient(ellipse at 85% 70%, rgba(79,158,143,0.45), rgba(79,158,143,0) 60%),
      radial-gradient(ellipse at 75% 95%, rgba(195,204,203,0.7), rgba(195,204,203,0) 55%);
  }
</style>
</head>
<body>
<main class="letterhead">
  <header>
    <div class="brand">
      <span class="brand-mark"></span>
      <span class="brand-name">
        <span class="firm">Quillfen</span>
        <span class="entity">Law Firm, P.C.</span>
      </span>
    </div>
    <ul class="contact-top">
      <li>
        <svg class="icon" viewBox="0 0 16 16"><circle cx="8" cy="8" r="6"/></svg>
        <span class="sep"></span>social.example/quillfenlaw
      </li>
      <li>
        <svg class="icon" viewBox="0 0 16 16"><rect x="1" y="3.5" width="14" height="9" rx="1"/><path d="M1.5 4.5 8 9l6.5-4.5" fill="none" stroke="#fff" stroke-width="1.3"/></svg>
        <span class="sep"></span>office@quillfenlaw.example
      </li>
      <li>
        <svg class="icon" viewBox="0 0 16 16"><circle cx="8" cy="8" r="7"/><path d="M1 8h14M8 1c-3 3.5-3 10.5 0 14M8 1c3 3.5 3 10.5 0 14" fill="none" stroke="#fff" stroke-width="0.9"/></svg>
        <span class="sep"></span>www.quillfenlaw.example
      </li>
    </ul>
    <div class="rule-top"></div>
  </header>

  <div class="branch-art" role="img" aria-label="Branching lightning illustration in teal and soft grey"></div>

  <footer>
    <div class="rule-bottom"></div>
    <ul class="contact-bottom">
      <li>
        <svg class="icon" viewBox="0 0 16 16"><path d="M8 0.8a5 5 0 0 0-5 5c0 3.8 5 9.6 5 9.6s5-5.8 5-9.6a5 5 0 0 0-5-5z"/><circle cx="8" cy="5.8" r="1.9" fill="#fff"/></svg>
        <span class="sep"></span>8716 SW 19th Ave,<strong>Portland, OR 97058.</strong>
      </li>
      <li>
        <svg class="icon" viewBox="0 0 16 16"><path d="M3.6 1.2 6 1l1.3 3.4-1.6 1.2a9 9 0 0 0 4.7 4.7l1.2-1.6L15 10l-.2 2.4c-.1.9-.9 1.6-1.8 1.6C6.9 14 2 9.1 2 3c0-.9.7-1.7 1.6-1.8z"/></svg>
        <span class="sep"></span><span class="label">T</span>971 555 0143<span class="gap">|</span><span class="label">F</span>971 555 0178
      </li>
    </ul>
  </footer>
</main>
</body>
</html>
```